Stylish, Masculine Design - Men's Clothing

Granary Coat Mart is a 14,000 square foot warehouse outlet store open to the public since 2005. 50+ brands. Well-known designer brand names and private labels. 30-80% off retail everyday. Lowest prices guaranteed. Average suit price $150. Average shirt price $20. One-stop shop shopping. Men's suits, tuxedos, tuxedo rentals, dress shirts, ties, dress shoes, boy's suits and tuxedos, clergy robes, clergy shirts, cologne, loungewear. Slim fits (Prom Dance), business styles, "church" fashion, security-related uniform. Alterations done by expert tailors on premises for an extra charge.
The final design for both business card and logo should portray stylishness and masculinity.
Updates
We will be changing our name. Details below.New name: Warehouse Suit & TuxFormer name: Granary Coat Mart Added Monday, December 26, 2016
Target Market(s)
Gender: 80% Male, 15% Female, 5% Transgender
Location: 80% 10 Mile Radius, 20% >10 Mile Radius
Age: 17-18 (Primarily prom), 18-35 (Primarily Interviews and Weddings), 36-70 (primarily Church and events)
Race: African-American 50%, Latino-American 20%, White 15%, 10% Asian 5% Other
Religions: Christian 50%, 20% Catholic, 10% Mormon, 20% Other/None
Occupation: Local government 40%, Large corporation employee 20%, Small business employee 10%, Small business owner 10%, 20% Unemployed (high school, college)
Education: High School or equivalent 40%, College 30%, Some College 20%, Masters/Doctors 10%
Industry/Entity Type
Retail
Contact Information for Business Card
Name: Peter Olund
Title: Sales Associate
Address: 418 E. Mirabeth Ave. Brenwick, CA 93511
Phone Number: 310.555.0182
Slogan: Broad Racks. Honest Tags, Tailored Help Every Visit
www.granarycoatmart.example
Logo Text
GCM (Acronym for Granary Coat Mart) or Image
Requirements
Must have
- Easy to read
- Visually appealing

```html
<!DOCTYPE html>
<html lang="en">
<head>
<meta charset="utf-8">
<title>Granary Coat Mart – Business Card</title>
<link href="https://fonts.googleapis.com/css2?family=Open+Sans:wght@400;600;700&family=Tinos&display=swap" rel="stylesheet">
<style>
  :root {
    --backdrop: #d9d7d3;
    --card: #ffffff;
    --card-shade: #ececec;
    --brand-red: #e3141f;
    --ink: #1b1b1b;
    --ink-soft: #4a4a4a;
    --on-red: #ffffff;
  }
  html, body {
    margin: 0;
    padding: 0;
    width: 1200px;
    height: 1000px;
    overflow: hidden;
    background: var(--backdrop);
  }
  .card {
    position: absolute;
    left: 100px;
    top: 214px;
    width: 1000px;
    height: 572px;
    background: linear-gradient(135deg, var(--card) 0%, var(--card) 55%, var(--card-shade) 100%);
    box-shadow: 0 18px 40px rgba(0,0,0,0.25);
    overflow: hidden;
    font-family: "Open Sans", Arial, sans-serif;
  }
  .tie-art {
    position: absolute;
    left: 110px;
    top: 0;
    width: 70px;
    height: 290px;
    background: var(--brand-red);
  }
  .wordmark {
    position: absolute;
    left: 215px;
    top: 78px;
    margin: 0;
    font-weight: 700;
    color: var(--ink);
    line-height: 1;
    text-transform: uppercase;
  }
  .wordmark span { display: block; }
  .wordmark .line-1 { font-size: 52px; letter-spacing: 4px; }
  .wordmark .line-2 { font-size: 78px; letter-spacing: 1px; margin-top: 4px; }
  .contact {
    position: absolute;
    left: 70px;
    top: 360px;
    margin: 0;
    padding: 0;
    list-style: none;
  }
  .contact li {
    display: flex;
    align-items: center;
    gap: 14px;
    margin-bottom: 12px;
    font-size: 22px;
    color: var(--ink-soft);
  }
  .contact .phone-number { font-family: "Tinos", "Times New Roman", serif; font-size: 24px; }
  .contact svg { width: 26px; height: 26px; flex: none; }
  .person {
    position: absolute;
    right: 80px;
    top: 290px;
    text-align: right;
  }
  .person-name {
    margin: 0;
    font-size: 44px;
    font-weight: 600;
    color: var(--ink-soft);
    letter-spacing: -0.5px;
  }
  .person-name .given { color: var(--brand-red); }
  .person-role {
    margin: 2px 0 0;
    font-size: 22px;
    letter-spacing: 7px;
    color: var(--ink-soft);
  }
  .address {
    position: absolute;
    right: 80px;
    top: 420px;
    text-align: right;
    font-style: normal;
    font-size: 22px;
    line-height: 1.25;
    color: var(--ink-soft);
  }
  .address-label {
    display: block;
    color: var(--brand-red);
    font-weight: 700;
    font-size: 20px;
  }
  .footer-band {
    position: absolute;
    left: 0;
    bottom: 0;
    width: 1000px;
    height: 44px;
  }
  .slogan {
    position: absolute;
    left: 80px;
    bottom: 11px;
    margin: 0;
    font-size: 17px;
    color: var(--on-red);
    letter-spacing: 0.3px;
  }
</style>
</head>
<body>
  <article class="card">
    <div class="tie-art" role="img" aria-label="Red necktie illustration"></div>

    <h1 class="wordmark">
      <span class="line-1">Granary</span>
      <span class="line-2">Coat Mart</span>
    </h1>

    <ul class="contact">
      <li>
        <svg viewBox="0 0 26 26" aria-hidden="true">
          <rect width="26" height="26" rx="4" fill="var(--brand-red)"/>
          <path d="M8 6c1 0 2 2.5 2 3.2s-1.2 1.2-1 2c.6 2 2.4 3.8 4.4 4.4.8.2 1.3-1 2-1s3.2 1 3.2 2-1.6 3-3 2.8C10.6 19 7 15.4 6.2 10.4 6 8.2 7 6 8 6z" fill="#fff"/>
        </svg>
        <span class="phone-number">310.555.0182</span>
      </li>
      <li>
        <svg viewBox="0 0 26 26" aria-hidden="true">
          <rect width="26" height="26" rx="4" fill="var(--brand-red)"/>
          <circle cx="13" cy="13" r="7" fill="none" stroke="#fff" stroke-width="1.8"/>
          <path d="M6 13h14M13 6c-3 3.5-3 10.5 0 14M13 6c3 3.5 3 10.5 0 14" fill="none" stroke="#fff" stroke-width="1.4"/>
        </svg>
        <span class="web">granarycoatmart.example</span>
      </li>
    </ul>

    <div class="person">
      <p class="person-name"><span class="given">Peter</span>Olund</p>
      <p class="person-role">Sales Associate</p>
    </div>

    <address class="address">
      <span class="address-label">Address</span>
      418 E. Mirabeth Ave<br>
      Brenwick, CA 93511
    </address>

    <svg class="footer-band" viewBox="0 0 1000 44" aria-hidden="true">
      <path d="M0 8 H58 L66 0 L74 8 H1000 V44 H0 Z" fill="var(--brand-red)"/>
    </svg>
    <p class="slogan">Broad Racks. Honest Tags, Tailored Help Every Visit</p>
  </article>
</body>
</html>
```